Hardcore nerd needs to stand out in a sea of dull Defence business cards

Wombeck Dynamics is a new Australian consulting engineering company that turns research and theory into practical systems. No evangelistic fluff, just mathematics and physics into electronic and optical circuits for consumer products, scientific research or Defence applications.

We already have a recognised logo (provided) which is often dark blue/black on a light background but we're open to other combinations. (Us engineers tend to have limited aesthetic imagination :)

Some of our recent products have included:
* Instrumentation for electrical testing,
* Radar jammers,
* GPS antenna design,
* Satellite tracking systems,
* High power lasers

We're open to both single and double-sided designs - happy to be convinced either way.

P.S. Another group is working on the web page, so - alas - our web site is currently of no use for images/ideas...

Target Market(s)

Engineering managers,
Scientists

Contact Information for Business Card

Dr Martin Folsey
R&D Engineer

martin@wombeckdynamics.com.au
0427 563 201

PO Box XXX (to be confirmed)
Brindlow ACT 2914
Australia

Font styles to use
Serif
Sans Serif

Colors

Designer to choose colors to be used in the design.

Requirements
Must have
• My contact details!
• I've had many (great) "bold and plain" designs submitted already, so feel free to be artistically creative :)
• Happy to take advice re fonts/colours/printability etc.
Nice to have
• I'm not sure if "lists" are more at home on a CV than a business card, but representative services include:
• Applied electromagnetics
• RF and high speed electronics
• Signal and image processing
• Electro-optical and laser systems
• Concept-to-prototype design services
• If you're considering double sided cards, then often measuring/alignment grids/rulers feature on the back of similar cards.
• e.g. https://www.kelvorin.com/newgrouppage9.cfm?objectgroup_id=4183
• https://www.kelvorin.com/newgrouppage9.cfm?objectgroup_ID=4185
• ..or even a "Smith chart" (google will return lots)
• Generic images to represent a capability might work - googling images associated with keyword for each of these areas might help:
• - "passive radar", "phased array", "fdtd", "vircator"
• RF and high speed electronic design
• - "smith chart", "microstrip circuits", "dimensioned drawing", "electronic schematic"
• - "dft", "iir filter"
• - "optical cavity". "laser energy level diagram"
• Background/watermarked images outlines/wireframes/schematics would probably look OK.
Should not have
• If a list of projects/services is provided, it is important not to make the client feel that this is "all" the company can do. Engineering design is a creative discipline (like graphics :)
• Please, no stock "military" snaps like planes, missiles, etc!

```html
<!DOCTYPE html>
<html lang="en">
<head>
<meta charset="utf-8">
<title>Wombeck Dynamics – Business Card</title>
<link href="https://fonts.googleapis.com/css2?family=Montserrat:wght@400;700&display=swap" rel="stylesheet">
<style>
  :root {
    --backdrop: #3a3430;
    --card: #2c2d2f;
    --gloss: #141415;
    --ink: #f2f2f2;
    --ink-soft: #c9c9c9;
    --rule: #d9d9d9;
  }
  * { margin: 0; padding: 0; box-sizing: border-box; }
  html, body {
    width: 1200px; height: 716px; overflow: hidden;
    background: var(--backdrop);
    font-family: "Montserrat", sans-serif;
  }
  .sheet {
    width: 1200px; height: 716px;
    display: flex; align-items: center; justify-content: center; gap: 40px;
  }
  .card {
    position: relative;
    width: 540px; height: 309px;
    background: var(--card);
    box-shadow: 0 10px 30px rgba(0,0,0,.45);
  }
  .brand {
    position: absolute;
    display: flex; align-items: center; gap: 12px;
  }
  .brand-dot { border-radius: 50%; flex: none; }
  .brand-name {
    font-weight: 700; letter-spacing: 1px; text-transform: uppercase; line-height: 1.05;
  }

  /* front */
  .card-front .brand { left: 50%; top: 50%; transform: translate(-50%, -50%); }
  .card-front .brand-dot { width: 64px; height: 64px; background: var(--gloss); }
  .card-front .brand-name { font-size: 28px; color: var(--gloss); }

  /* back */
  .card-back .brand { right: 40px; top: 62px; gap: 10px; }
  .card-back .brand-dot { width: 48px; height: 48px; background: var(--ink); }
  .card-back .brand-name { font-size: 18px; color: var(--ink); }

  .person { position: absolute; left: 40px; top: 82px; color: var(--ink); }
  .person-name { font-size: 17px; font-weight: 700; letter-spacing: .5px; text-transform: uppercase; white-space: nowrap; }
  .person-title { font-size: 10px; color: var(--ink-soft); margin-top: 2px; }

  .divider {
    position: absolute; left: 40px; right: 40px; top: 140px;
    height: 1px; background: var(--rule);
  }
  .contact {
    position: absolute; left: 40px; top: 156px;
    list-style: none; font-size: 11px; color: var(--ink-soft);
  }
  .contact li { display: flex; align-items: center; gap: 7px; margin-bottom: 5px; }
  .contact svg { width: 10px; height: 10px; fill: var(--ink-soft); }
  .address {
    position: absolute; left: 330px; top: 218px;
    font-style: normal; font-size: 11.5px; line-height: 1.45; color: var(--ink-soft);
  }
</style>
</head>
<body>
<main class="sheet">
  <section class="card card-front" aria-label="Card front">
    <div class="brand">
      <span class="brand-dot"></span>
      <span class="brand-name">Wombeck<br>Dynamics</span>
    </div>
  </section>

  <section class="card card-back" aria-label="Card back">
    <div class="person">
      <p class="person-name">Dr Martin Folsey</p>
      <p class="person-title">R&amp;D Engineer</p>
    </div>
    <div class="brand">
      <span class="brand-dot"></span>
      <span class="brand-name">Wombeck<br>Dynamics</span>
    </div>
    <div class="divider"></div>
    <ul class="contact">
      <li>
        <svg viewBox="0 0 24 24" aria-hidden="true"><path d="M6.6 10.8a15 15 0 0 0 6.6 6.6l2.2-2.2a1 1 0 0 1 1-.25 11.4 11.4 0 0 0 3.6.57 1 1 0 0 1 1 1V20a1 1 0 0 1-1 1A17 17 0 0 1 3 4a1 1 0 0 1 1-1h3.5a1 1 0 0 1 1 1c0 1.250.2 2.450.57 3.57a1 1 0 0 1-.25 1z"/></svg>
        0427 563 201
      </li>
      <li>
        <svg viewBox="0 0 24 24" aria-hidden="true"><path d="M2 5h20v14H2zm2 2v.5l8 5 8-5V7zm0 3v7h16v-7l-8 5z"/></svg>
        martin@wombeckdynamics.com.au
      </li>
    </ul>
    <address class="address">
      PO Box XXX<br>
      Brindlow ACT 2914, Australia
    </address>
  </section>
</main>
</body>
</html>
```